Local Flower Farm Needs Business Card Design

I need business cards designed for a flower farm based in Eudora, Kansas.
Business Info:
We are a local cut flower farm located in Eudora, Kansas, founded by Darla Hoffstrom. What started as a passion for agriculture and search for more joy in daily life has blossomed into a small business dedicated to providing the community with beautiful, fresh, and sustainable flowers. We specialize in local, seasonal blooms, ensuring that every petal reflects the care and dedication we pour into our craft. Our mission is to deliver the highest quality flowers directly to our customers through local farmers markets and to florists who share our commitment to sustainability. Join us in celebrating the beauty of nature, one bloom at a time!
Contact Details:
Darla Hoffstrom
Owner
Phone 913-555-0147
Facebook: Lorabelle Quinn Blossoms
Instagram: @LorabelleQuinnBlossoms
Website: LorabelleQuinnBlossoms.example
Target Market(s)
Wholesale to Florists and Direct to Consumer via Farmers Market
Industry/Entity Type
Florist, Farm
Contact Information for Business Card
Name, Contact Info, Logo
Look and feel

```html
<!DOCTYPE html>
<html lang="en">
<head>
<meta charset="utf-8">
<title>Lorabelle Quinn Blossoms – Business Card</title>
<link rel="stylesheet" href="https://fonts.googleapis.com/css2?family=Tinos:wght@400;700&display=swap">
<style>
  :root {
    --backdrop: #2f2f2f;
    --forest: #0d2529;
    --paper: #ffffff;
    --ink: #0f2226;
    --rule: #1a1a1a;
    --cream: #f4f1ea;
  }
  * { box-sizing: border-box; margin: 0; padding: 0; }
  html, body {
    width: 1200px; height: 689px; overflow: hidden;
    background: var(--backdrop);
    font-family: "Tinos", "Times New Roman", serif;
  }
  .canvas { position: relative; width: 1200px; height: 689px; }

  .card {
    position: absolute; top: 193px;
    width: 530px; height: 303px;
    border-radius: 26px;
    box-shadow: 0 18px 40px rgba(0,0,0,.45);
    overflow: hidden;
  }
  .card--front { left: 50px; background: var(--forest); }
  .card--back  { left: 620px; background: var(--paper); }

  /* brand seal: ring plus set wordmark */
  .seal {
    position: absolute;
    display: flex; flex-direction: column; align-items: center; justify-content: center;
    border-radius: 50%;
    text-transform: uppercase; text-align: center;
    font-weight: 400;
  }
  .card--front .seal {
    width: 200px; height: 200px; left: 165px; top: 51px;
    border: 1px solid var(--cream); color: var(--cream);
    font-size: 17px; letter-spacing: 3px; line-height: 1.5;
  }
  .card--back .seal {
    width: 130px; height: 130px; left: 350px; top: 16px;
    border: 1px solid var(--ink); color: var(--ink);
    font-size: 11px; letter-spacing: 2px; line-height: 1.5;
  }

  .identity { position: absolute; left: 28px; top: 120px; color: var(--ink); }
  .identity__name { font-size: 30px; font-weight: 700; line-height: 1.1; }
  .identity__role { font-size: 13px; margin-top: 4px; margin-left: 18px; font-weight: 400; }

  .divider {
    position: absolute; left: 30px; right: 22px; top: 186px;
    border-top: 1px solid var(--rule);
  }

  .contacts { position: absolute; left: 40px; top: 195px; list-style: none; color: var(--ink); }
  .contacts__item {
    display: flex; align-items: center; gap: 8px;
    font-size: 14px; line-height: 22px;
  }
  .contacts__marker { width: 11px; height: 11px; flex: none; }
  .contacts__marker--phone { fill: var(--ink); }
  .contacts__marker--square { background: #3b5a9a; border-radius: 2px; }
  .contacts__marker--square-alt { background: #c2366e; border-radius: 3px; }
  .contacts__marker--circle { border-radius: 50%; background: var(--ink); }
</style>
</head>
<body>
<main class="canvas">
  <section class="card card--front" aria-label="Card front">
    <div class="seal">
      <span>Lorabelle Quinn</span>
      <span>Blossoms</span>
    </div>
  </section>

  <section class="card card--back" aria-label="Card back">
    <div class="seal">
      <span>Lorabelle Quinn</span>
      <span>Blossoms</span>
    </div>

    <div class="identity">
      <h1 class="identity__name">Darla Hoffstrom</h1>
      <p class="identity__role">Owner</p>
    </div>

    <div class="divider"></div>

    <ul class="contacts">
      <li class="contacts__item">
        <svg class="contacts__marker contacts__marker--phone" viewBox="0 0 24 24" aria-hidden="true"><path d="M6.6 10.8a15.1 15.1 0 0 0 6.6 6.6l2.2-2.2a1 1 0 0 1 1-.25 11.4 11.4 0 0 0 3.6.57 1 1 0 0 1 1 1V20a1 1 0 0 1-1 1A17 17 0 0 1 3 4a1 1 0 0 1 1-1h3.5a1 1 0 0 1 1 1c0 1.25.2 2.45.57 3.6a1 1 0 0 1-.25 1z"/></svg>913-555-0147
      </li>
      <li class="contacts__item"><span class="contacts__marker contacts__marker--square"></span>Lorabelle Quinn Blossoms</li>
      <li class="contacts__item"><span class="contacts__marker contacts__marker--square-alt"></span>@LorabelleQuinnBlossoms</li>
      <li class="contacts__item"><span class="contacts__marker contacts__marker--circle"></span>LorabelleQuinnBlossoms.example</li>
    </ul>
  </section>
</main>
</body>
</html>
```